Hair dresser flyer for Air conditioning heat pumps A5

We require a flyer that is selling the benifits of air conditioning heat pumps which cools in summer and efficently heats in winter. Colour should be white background. Red and blue from logo to represent the Air conditioning Heat pump does heating and cooling and energy effient.

Target Market(s)

Hairdressor, Salons , barbers ,

Colors
0054AA
0677BA
7BADD7
CADEEF
E8F1F8
EB3D1F
EC4F4E
F09395
F8D3D4
FCEDEE

Requirements
Must have
• Cost from

```html
<!DOCTYPE html>
<html lang="en">
<head>
<meta charset="utf-8">
<title>Kelvin – Air Conditioning Heat Pumps Flyer</title>
<link href="https://fonts.googleapis.com/css2?family=Roboto:wght@300;400;500;700&display=swap" rel="stylesheet">
<style>
  :root{
    --blue:#3aa3dc;
    --orange:#e84f24;
    --red:#EB3D1F;
    --pink:#F8D3D4;
    --ink:#1c1c1c;
    --white:#ffffff;
    --backdrop:#dfe4e8;
  }
  *{box-sizing:border-box;margin:0;padding:0}
  html,body{width:1200px;height:2492px;overflow:hidden;background:var(--backdrop);font-family:'Roboto',sans-serif}
  .sheet{position:absolute;left:209px;width:810px;height:1145px;overflow:hidden;background:var(--white);box-shadow:0 10px 30px rgba(0,0,0,.18)}
  .sheet--front{top:55px}
  .sheet--back{top:1262px}
  .sheet__inner{position:absolute;left:0;top:0;width:648px;height:916px;transform:scale(1.25);transform-origin:0 0}
  .art{position:absolute;left:0;top:0;width:648px;height:916px}
  .brand{position:absolute;display:flex;align-items:center;gap:10px;font-weight:500;font-size:38px;line-height:1;color:var(--ink)}
  .brand__dot{width:14px;height:14px;border-radius:50%;background:var(--blue)}
  .front .brand{left:384px;top:48px}
  .back .brand{left:42px;top:50px}
  .headline{position:absolute;right:38px;top:158px;text-align:right;color:var(--ink);font-weight:300;font-size:25px;line-height:30px}
  .headline__big{font-size:38px;font-weight:500;line-height:44px;letter-spacing:.5px}
  .hot{color:var(--red);font-weight:500}
  .cool{color:var(--blue);font-weight:500}
  .offer{position:absolute;right:42px;top:344px;text-align:right;font-size:17px;font-weight:300;line-height:22px;color:var(--ink)}
  .offer strong{color:var(--red);font-weight:700}
  .benefits{position:absolute;left:40px;top:454px;list-style:none;color:var(--white);font-weight:700;font-size:14.5px;line-height:23px}
  .benefits li{display:flex;align-items:center;gap:9px}
  .benefits svg{width:14px;height:14px}
  .copy{position:absolute;left:42px;width:570px;font-weight:300;font-size:15px;line-height:18.4px}
  .copy p+p{margin-top:18px}
  .front .copy{top:664px;color:var(--white)}
  .back .intro{top:134px;color:var(--ink)}
  .compare{position:absolute;left:42px;top:690px;color:var(--white);font-weight:700;font-size:14.5px;line-height:23px}
  .compare p+p{margin-top:23px}
  .back .contact{top:838px;color:var(--white)}
  .contact b{font-weight:700;font-style:italic}
</style>
</head>
<body>

<section class="sheet sheet--front">
  <div class="sheet__inner front">
    <svg class="art" viewBox="0 0 648 916">
      <path d="M0 0H358C335 130 300 300 180 405L0 412Z" fill="#d9b6ae" role="img" aria-label="Photo of a wall-mounted air conditioning unit inside a pink salon"/>
      <path d="M358 0C335 130 300 300 180 405L198 410C320 310 355 150 372 0Z" fill="var(--orange)"/>
      <path d="M330 505C420 555 540 560 648 540V560C540 590 420 580 330 520Z" fill="var(--orange)"/>
      <path d="M0 412C100 410 160 405 188 408C260 490 380 545 648 555V916H0Z" fill="var(--blue)"/>
      <circle cx="441" cy="534" r="116" fill="var(--white)"/>
      <circle cx="441" cy="534" r="110" fill="#8a8f94" role="img" aria-label="Photo of a dark air conditioning heat pump unit"/>
    </svg>

    <div class="brand"><span class="brand__dot"></span>Kelvin</div>

    <h1 class="headline">
      <span class="headline__big">SAVE £££</span><br>
      on your Shops<br>
      <span class="hot">Heating</span> costs<br>
      And stay <span class="cool">Cool</span><br>
      in the Summer
    </h1>

    <p class="offer">Energy- Efficient Air Conditioning Heat<br>Pumps installed from <strong>£1750 + Vat</strong></p>

    <ul class="benefits">
      <li><svg viewBox="0 0 14 14"><path d="M1 7.5L5 11.5L13 2.5" fill="none" stroke="#fff" stroke-width="2.2"/></svg>Cools in Summer</li>
      <li><svg viewBox="0 0 14 14"><path d="M1 7.5L5 11.5L13 2.5" fill="none" stroke="#fff" stroke-width="2.2"/></svg>Efficient Heats in Winter</li>
      <li><svg viewBox="0 0 14 14"><path d="M1 7.5L5 11.5L13 2.5" fill="none" stroke="#fff" stroke-width="2.2"/></svg>More Productive staff</li>
      <li><svg viewBox="0 0 14 14"><path d="M1 7.5L5 11.5L13 2.5" fill="none" stroke="#fff" stroke-width="2.2"/></svg>Increased Sales</li>
      <li><svg viewBox="0 0 14 14"><path d="M1 7.5L5 11.5L13 2.5" fill="none" stroke="#fff" stroke-width="2.2"/></svg>Reduce cancellation in Summer</li>
      <li><svg viewBox="0 0 14 14"><path d="M1 7.5L5 11.5L13 2.5" fill="none" stroke="#fff" stroke-width="2.2"/></svg>Filters and cleans the air</li>
      <li><svg viewBox="0 0 14 14"><path d="M1 7.5L5 11.5L13 2.5" fill="none" stroke="#fff" stroke-width="2.2"/></svg>Reduced allergens &amp; Bugs</li>
      <li><svg viewBox="0 0 14 14"><path d="M1 7.5L5 11.5L13 2.5" fill="none" stroke="#fff" stroke-width="2.2"/></svg>Reduce Humidity</li>
    </ul>

    <div class="copy">
      <p>Air Conditioning Heat Pumps creates the ideal environment all year round for staff to be at there most productive and for consumers to spend more time and, accordingly, more money.</p>
      <p>Modern Air Conditioning Heat pumps are one of the most energy efficient forms of heating available and ideal for those looking for a simple cost effective way to heat and cool the space. They are easy to install &nbsp;and operate and can quickly provide with the comfort you need.</p>
      <p>Reduce cancelations and absences in the warm summer months with Cooling mode. With the warms temperatures inside hairdressers and salons and clients not wanting to sit in somewhere with extreme heat</p>
    </div>
  </div>
</section>

<section class="sheet sheet--back">
  <div class="sheet__inner back">
    <svg class="art" viewBox="0 0 648 916">
      <path d="M0 400C30 560 200 650 400 660C500 665 570 700 648 760V916H0Z" fill="var(--orange)"/>
      <ellipse cx="322" cy="505" rx="312" ry="152" fill="var(--blue)"/>
      <ellipse cx="328" cy="500" rx="300" ry="143" fill="var(--white)"/>
      <ellipse cx="335" cy="498" rx="292" ry="130" fill="var(--pink)"/>
      <circle cx="688" cy="495" r="276" fill="var(--white)"/>
      <circle cx="688" cy="495" r="266" fill="#e2cfd0" role="img" aria-label="Photo of a ceiling air conditioning unit above a flower display"/>
      <circle cx="325" cy="464" r="170" fill="#b9aea6" role="img" aria-label="Photo of a hair salon interior with a ceiling cassette heat pump"/>
    </svg>

    <div class="brand"><span class="brand__dot"></span>Kelvin</div>

    <div class="copy intro">
      <p>Reduce heating energy &nbsp;cost by up to 75% vs electric heating. Air conditioning heat pumps is a more efficient heating solution in comparison to a standard electric heaters which are still used in many businesses. This is because air conditioning produces more heat for the amount of electricity it takes to power the unit.</p>
      <p style="margin-top:26px">Here's an example to illustrate how an air-to-air heat<br>pump can save you money over an electric &nbsp;heaters</p>
    </div>

    <div class="compare">
      <p>2 x 2kw Eleectic fan heaters<br>4kw Electricity input &nbsp;= &nbsp;&nbsp;4kw heat Output</p>
      <p>4kw Air Conditioning heat pump<br>1kw Electricty input = &nbsp;&nbsp;4kw Heat output</p>
    </div>

    <p class="copy contact">If you are interested in having air conditioning installed in your &nbsp;business, then give us a call on <b>01632 960418</b> or visit our website <b>https://www.kelvinair.cool/</b>.</p>
  </div>
</section>

</body>
</html>
```